Law Firm Needs Brochure Redesign Using New Logo

We are a personal injury law firm that does auto injuries and other personal injury cases. We want a new brochure that has our updated logo and information. Instead of gold and black, we want more navy, as matches the new logo. The Auto Liability portion should read: "(required by the state of Arizona in the amounts of $25,000 per person / $50,000 per accident, but a higher amount may be best )." The other information can remain the same. We'd like the brochure to keep the same professional tone as the previous brochure.
Our website is https://www.marbrenlegal.com/.

```html
<!DOCTYPE html>
<html lang="en">
<head>
<meta charset="utf-8">
<title>Marbren Legal – Car Accident Brochure</title>
<link rel="stylesheet" href="https://fonts.googleapis.com/css2?family=Montserrat:wght@400;500;600;700&display=swap">
<style>
:root{
  --navy:#14213f;
  --navy-deep:#0f1a33;
  --navy-mid:#22325a;
  --ink-blue:#3b4a7c;
  --accent:#9fd0ee;
  --cyan-band:#d3f6fa;
  --teal:#5fd3e3;
  --grey:#ececec;
  --white:#ffffff;
  --page:#f1ece4;
}
*{box-sizing:border-box;margin:0;padding:0}
html,body{width:960px;height:1200px;overflow:hidden}
body{background:var(--page);font-family:'Montserrat',sans-serif;color:var(--navy);position:relative}
.sheet{position:absolute;left:152px;width:652px;height:504px;display:flex;box-shadow:0 4px 14px rgba(0,0,0,.18)}
.sheet--outside{top:77px}
.sheet--inside{top:620px}
.panel{position:relative;height:100%;overflow:hidden}
.fill{position:absolute;inset:0}
.brand{display:flex;align-items:center;gap:7px;font-weight:700;letter-spacing:.06em;text-transform:uppercase}
.brand-dot{width:12px;height:12px;border-radius:50%;flex:none}

/* outside */
.panel--stats{width:214px;color:var(--white);text-align:center}
.panel--stats .fill{background:linear-gradient(180deg,#1a2748 0%,#24345e 40%,#3e5487 62%,#2a3a66 82%,#1a2748 100%)}
.stat{position:absolute;left:0;right:0}
.stat-over{color:var(--accent);font-size:20px;font-weight:600;line-height:1}
.stat-num{color:var(--accent);font-size:44px;font-weight:600;line-height:1;letter-spacing:-.01em}
.stat-note{font-size:8.8px;line-height:11.5px;margin-top:1px;padding:0 28px}
.stat--crashes{top:33px}
.stat--deaths{top:148px}
.panel--stats .brand{position:absolute;top:272px;left:0;right:0;justify-content:center;font-size:15px;color:var(--white)}
.panel--stats .brand-dot{background:var(--white)}
.pitch{position:absolute;top:386px;left:24px;right:24px;font-size:8.8px;line-height:11px}
.pitch strong{display:block;font-size:11px;font-weight:600;margin-top:1px}

.panel--mailer{width:219px;background:var(--white)}
.panel--mailer .brand{position:absolute;left:23px;top:420px;font-size:14px;color:var(--navy)}
.panel--mailer .brand-dot{background:var(--navy)}
.mail-address{position:absolute;left:23px;top:457px;font-size:8.8px;line-height:11px;color:var(--navy)}

.panel--cover{width:219px;background:var(--navy-deep);color:var(--white);text-align:center}
.cover-photo{position:absolute;left:0;right:0;top:118px;height:300px;background:linear-gradient(160deg,#0f1a33 0%,#2b3d6b 35%,#111d3a 60%,#27386a 80%,#0f1a33 100%)}
.cover-title{position:absolute;top:38px;left:14px;right:14px;font-size:15.5px;font-weight:600;line-height:20px}
.cover-sub{position:absolute;top:83px;left:18px;right:18px;font-size:9.5px;line-height:12px;color:var(--accent);font-weight:400}
.panel--cover .brand{position:absolute;top:436px;left:0;right:0;justify-content:center;font-size:15px;color:var(--white)}
.panel--cover .brand-dot{background:var(--white)}

/* inside */
.band{background:var(--cyan-band);color:var(--navy);font-weight:600;font-size:11.5px;text-align:center;height:20px;line-height:20px;text-transform:uppercase}
.panel--tips{width:218px;background:var(--navy);color:var(--white)}
.panel--tips .band{margin-top:26px}
.tips{list-style:none;padding:12px 18px 0 12px;font-size:8.8px;line-height:11px}
.tips li{margin-bottom:11px}
.tips em{font-style:normal;color:var(--teal)}

.panel--coverage{width:219px;background:var(--white)}
.coverage-art{position:absolute;left:18px;right:18px;top:30px;height:168px;background:linear-gradient(180deg,#3f83cf 0%,#2c64b0 35%,#e6e8ec 60%,#ffffff 100%)}
.panel--coverage .band{position:absolute;top:208px;left:0;right:0}
.coverage-text{position:absolute;top:239px;left:10px;right:10px;font-size:8.8px;line-height:11px;color:var(--ink-blue)}
.coverage-text p{margin-bottom:11px}

.panel--safety{width:215px;background:var(--grey)}
.safety-photo{position:absolute;left:0;right:0;top:0;height:207px;background:linear-gradient(135deg,#6b6257 0%,#b9a48c 35%,#d9cfc4 55%,#8a8178 80%,#4a4744 100%)}
.panel--safety .band{position:absolute;left:0;right:0}
.band--model{top:207px}
.band--text{top:276px}
.band--contact{top:370px}
.safety-text{position:absolute;left:9px;right:8px;font-size:8.8px;line-height:11px;color:var(--ink-blue)}
.safety-text--buckle{top:233px}
.safety-text--phones{top:302px}
.safety-text p{margin-bottom:11px}
.contact-box{position:absolute;left:0;right:0;top:408px;height:77px;background:var(--navy);color:var(--white);text-align:center;font-size:8.8px;line-height:11px;padding-top:6px;font-style:normal}
</style>
</head>
<body>

<section class="sheet sheet--outside">
  <div class="panel panel--stats">
    <div class="fill" role="img" aria-label="Photo of a tree-lined country road stretching into the distance"></div>
    <div class="stat stat--crashes">
      <div class="stat-over">OVER</div>
      <div class="stat-num">107,000</div>
      <p class="stat-note">crashes will happen in the state of Arizona this year.</p>
    </div>
    <div class="stat stat--deaths">
      <div class="stat-over">OVER</div>
      <div class="stat-num">700</div>
      <p class="stat-note">of them will result in fatalities.</p>
    </div>
    <div class="brand"><span class="brand-dot"></span>Marbren Legal</div>
    <p class="pitch">If we don't win, you don't pay attorney fees. That seems fair to us. Know what's happening with your case, get the answers to your questions and work on getting better with the confidence that you've got an excellent group of <strong>people working for you.</strong></p>
  </div>

  <div class="panel panel--mailer">
    <div class="brand"><span class="brand-dot"></span>Marbren Legal</div>
    <p class="mail-address">4810 N. 19th Avenue Suite B104<br>Phoenix AZ 85015</p>
  </div>

  <div class="panel panel--cover">
    <h1 class="cover-title">Protect your family in case of a car accident</h1>
    <p class="cover-sub">A little knowledge and preparation go a long way</p>
    <div class="cover-photo" role="img" aria-label="Close-up photo of the front of a glossy dark car"></div>
    <div class="brand"><span class="brand-dot"></span>Marbren Legal</div>
  </div>
</section>

<section class="sheet sheet--inside">
  <div class="panel panel--tips">
    <h2 class="band">Top 10 Tips to Avoid a Crash</h2>
    <ol class="tips">
      <li>1. <em>Anyone making a left turn must wait for all oncoming traffic to clear before proceeding.</em> Yes, even if the light has turned yellow. Wait to be sure that all traffic has stopped.</li>
      <li>2. <em>When your light turns green</em>, check to be sure that no vehicles are entering the intersection late.</li>
      <li>3. <em>Allow plenty of room between you and the car in front of you.</em> Traffic can stop in an instant, even if you can’t see anything ahead.</li>
      <li>4. <em>Avoid being distracted.</em> Teenagers are especially susceptible to losing focus if there are too many friends in the car.</li>
      <li>5. <em>Keep the volume of your radio down and never wear headphones.</em> Cars are very soundproof these days, but you need to be able to hear an ambulance or police siren.</li>
      <li>6. <em>Be especially careful on the weekends and early morning hours.</em></li>
      <li>7. <em>Don’t speed.</em> Speed is a factor in most crashes. Street lights are timed and the freeway has traffic. It’s likely you won’t get there much faster even if you do speed.</li>
      <li>8. <em>Don’t drink and drive.</em> Many cab companies offer a free service to get you home safe.</li>
      <li>9. <em>Use your turn signals.</em> This gives an early warning to vehicles you may not be able to see.</li>
    </ol>
  </div>

  <div class="panel panel--coverage">
    <div class="coverage-art" role="img" aria-label="Illustration of a blue umbrella sheltering a white sedan"></div>
    <h2 class="band">Have the Right Coverage</h2>
    <div class="coverage-text">
      <p>Many people don’t know about the different kinds of insurance available. In addition to health insurance, we suggest:</p>
      <p>Auto Liability (required by the state of Arizona in the amounts of $25,000 per person / $50,000 per accident, but a higher amount may be best )</p>
      <p>Uninsured or Underinsured Motorist Coverage. This protects YOU when the other driver doesn’t have insurance or not enough.</p>
      <p>Medical Payments Coverage. Up to $5,000 in coverage will be paid out to you no matter who is at fault in an accident and does not need to be reimbursed.</p>
      <p>Homeowners / Renters Insurance. Protects you in case of injuries on your property as well as damage to your home from covered events.</p>
    </div>
  </div>

  <div class="panel panel--safety">
    <div class="safety-photo" role="img" aria-label="Photo of a smiling driver fastening her seat belt in a car"></div>
    <h2 class="band band--model">Model Safe Behavior</h2>
    <div class="safety-text safety-text--buckle">
      <p>Always buckle up. Always put your children in car seats/boosters that are rated for their height and weight.</p>
    </div>
    <h2 class="band band--text">Never Text While Driving</h2>
    <div class="safety-text safety-text--phones">
      <p>Studies have shown that texting while driving is as dangerous as driving intoxicated.</p>
      <p>Show your children that no text is more important than your safety. It can wait.</p>
    </div>
    <h2 class="band band--contact">Contact Us</h2>
    <address class="contact-box">
      Marbren Legal Group<br>
      4810 N. 19th Avenue Suite B104<br>
      Phoenix AZ 85015<br>
      602.555.0147<br>
      info@MarbrenLegal.com<br>
      www.marbrenlegal.com
    </address>
  </div>
</section>

</body>
</html>
```